Qorvane Advisory Corporate Brochure

Qorvane Advisory is a management consulting firm.

We need a corporate brochure showcasing our methodologies (two process diagrams) and our leadership team.

We would like it to look corporate, professional, clean and contemporary.

Happy to have duo tones using our Qorvane logo colours or mono pics.

Also like texture and 3 dimensional backgrounds and graphics.

We are waiting for head and shoulder photos of a couple of our Associate Directors (can you use placeholders while we obtain these please?)

Our web site is:

www.qorvaneadvisory.com.au

Thanks for your ideas.

Industry/Entity Type

Management Consulting

```html
<!DOCTYPE html>
<html lang="en">
<head>
<meta charset="utf-8">
<title>Qorvane Advisory – Folder Cover</title>
<link rel="stylesheet" href="https://fonts.googleapis.com/css2?family=Open+Sans:wght@400;600;700&display=swap">
<style>
  :root {
    --teal-dark: #115f66;
    --teal-mid: #14697a;
    --teal-light: #18748e;
    --teal-line: #0f5a68;
    --grey-line: #8a8f96;
    --white: #ffffff;
    --paper: #f7f7f5;
    --stage: #e9e6e1;
    --ink-grey: #6b7077;
    --illus-green: #9ccc3a;
    --illus-orange: #f07a28;
    --illus-yellow: #f7b52a;
    --illus-sky: #dfeef0;
  }
  * { margin: 0; padding: 0; box-sizing: border-box; }
  html, body { width: 1200px; height: 900px; overflow: hidden; }
  body {
    background: var(--stage);
    font-family: "Open Sans", Arial, sans-serif;
    position: relative;
  }
  .folder {
    position: absolute;
    left: 80px; top: 80px;
    width: 1040px; height: 740px;
    display: flex;
  }
  .cover { position: relative; width: 520px; height: 740px; overflow: hidden; }

  /* back cover */
  .cover--back {
    background: linear-gradient(180deg, var(--teal-dark) 0%, var(--teal-mid) 60%, var(--teal-light) 100%);
    color: var(--white);
  }
  .follow {
    position: absolute; left: 190px; top: 240px;
    font-weight: 700; font-size: 15px;
  }
  .follow-arrow { position: absolute; left: 300px; top: 258px; }
  .social {
    position: absolute; left: 200px; top: 285px;
    display: flex; align-items: center; gap: 8px;
    font-weight: 700; font-size: 16px;
  }
  .social-square { width: 18px; height: 18px; background: var(--white); border-radius: 3px; }
  .back-brand {
    position: absolute; left: 26px; top: 600px;
    display: flex; align-items: center; gap: 8px;
    font-weight: 600; font-size: 17px;
  }
  .brand-circle { width: 22px; height: 22px; border-radius: 50%; border: 3px solid currentColor; }
  .tagline {
    position: absolute; left: 26px; top: 668px;
    font-size: 8px; letter-spacing: .3px; word-spacing: 8px;
  }
  .contact {
    position: absolute; top: 680px;
    display: flex; gap: 6px; align-items: flex-start;
    font-size: 8.5px; line-height: 1.5; text-transform: none;
  }
  .contact--address { left: 185px; text-transform: uppercase; }
  .contact--phone { left: 380px; }

  /* front cover */
  .cover--front { background: var(--paper); }
  .cover-art { position: absolute; inset: 0; }
  .front-brand {
    position: absolute; left: 48px; top: 50px;
    display: flex; align-items: center; gap: 10px;
    color: var(--teal-line);
    font-weight: 600; font-size: 24px;
  }
  .front-brand .brand-circle { width: 30px; height: 30px; border-width: 5px; }
  .web {
    position: absolute; left: 0; right: 0; bottom: 22px;
    text-align: center; color: var(--white);
    font-size: 11px; font-weight: 600; letter-spacing: .2px;
  }
</style>
</head>
<body>
  <main class="folder">
    <section class="cover cover--back">
      <p class="follow">Follow us on:</p>
      <svg class="follow-arrow" width="50" height="70" viewBox="0 0 50 70" aria-hidden="true">
        <path d="M2 4 C40 6 48 52 12 62" fill="none" stroke="#fff" stroke-width="2"/>
        <path d="M20 54 L10 63 L22 67" fill="none" stroke="#fff" stroke-width="2"/>
      </svg>
      <div class="social"><span class="social-square"></span><span>Linkwell</span></div>

      <div class="back-brand"><span class="brand-circle"></span><span>Qorvane Advisory</span></div>
      <p class="tagline">People Process Outcomes</p>

      <div class="contact contact--address">
        <svg width="10" height="14" viewBox="0 0 10 14" aria-hidden="true">
          <path d="M5 0 C2 0 0 2.2 0 5 C0 8.5 5 14 5 14 C5 14 10 8.5 10 5 C10 2.2 8 0 5 0Z" fill="#fff"/>
          <circle cx="5" cy="5" r="2" fill="#14697a"/>
        </svg>
        <p>L12 Harbour Point, 40-44<br>Kestrel Street Perth WA 6000</p>
      </div>
      <div class="contact contact--phone">
        <svg width="12" height="14" viewBox="0 0 12 14" aria-hidden="true">
          <path d="M3 1 L5 4 L3.5 5.5 C4.5 7.5 5.5 8.5 7.5 9.5 L9 8 L12 10 L10.5 12.5 C6 12.5 1 7.5 1 3Z" fill="#fff"/>
        </svg>
        <p>+61 8 9000 4172<br>info@qorvaneadvisory.com.au</p>
      </div>
    </section>

    <section class="cover cover--front">
      <svg class="cover-art" width="520" height="740" viewBox="0 0 520 740">
        <defs>
          <linearGradient id="illusTone" x1="0" y1="0" x2="1" y2="1">
            <stop offset="0" stop-color="#a9d24a"/>
            <stop offset=".35" stop-color="#dfeef0"/>
            <stop offset=".7" stop-color="#f4a43a"/>
            <stop offset="1" stop-color="#2d97a8"/>
          </linearGradient>
          <linearGradient id="baseTeal" x1="0" y1="0" x2="0" y2="1">
            <stop offset="0" stop-color="#125f66"/>
            <stop offset="1" stop-color="#18748e"/>
          </linearGradient>
        </defs>
        <g role="img" aria-label="Illustration area: colourful growth scene with gears, rising arrow, bar chart, speech clouds and the word Growth">
          <path d="M0 170 C120 125 260 135 360 125 C430 118 490 130 520 150 L520 600 L0 600Z" fill="url(#illusTone)"/>
        </g>
        <path d="M0 160 C120 118 260 126 360 116 C430 110 490 122 520 142" fill="none" stroke="var(--teal-line)" stroke-width="4"/>
        <path d="M0 168 C120 126 260 134 360 124 C430 118 490 130 520 150" fill="none" stroke="var(--teal-line)" stroke-width="1.5"/>
        <path d="M0 620 C90 580 200 560 300 570 C400 580 470 560 520 540 L520 740 L0 740Z" fill="url(#baseTeal)"/>
        <path d="M0 588 C100 560 220 548 320 552 C420 556 480 536 520 520" fill="none" stroke="var(--teal-line)" stroke-width="4"/>
        <path d="M0 600 C100 572 220 560 320 564 C420 568 480 548 520 532" fill="none" stroke="var(--grey-line)" stroke-width="3"/>
      </svg>
      <div class="front-brand"><span class="brand-circle"></span><span>Qorvane Advisory</span></div>
      <p class="web">www.qorvaneadvisory.com.au</p>
    </section>
  </main>
</body>
</html>
```